Property development business card design

New build residential property developers. I want a professional look but customer friendly so not too corporate. I'm not sure what logo will look best so open to designs with either. Thank you

Also i don't want both names on one card its 2 names for 2 different cards but with the same design.

Industry/Entity Type

Residential

Contact Information for Business Card

TRW Developments Ltd,
58 Fennick Lane,
Ipswich,
Suffolk,
IP7 2DX

Property Research Manager
Judith Penrow

Managing Director
Dermot Aldwick

```html
<!DOCTYPE html>
<html lang="en">
<head>
<meta charset="utf-8">
<title>TRW Developments – Business Card</title>
<link rel="stylesheet" href="https://fonts.googleapis.com/css2?family=Exo+2:wght@400;500;600&family=Open+Sans:wght@400;700&display=swap">
<style>
  :root {
    --page-bg: #e9eaec;
    --card-bg: #ffffff;
    --brand-blue: #2f7fd0;
    --band-deep: #3a3fb0;
    --band-light: #27a6e6;
    --name-blue: #3d3f96;
    --ink: #2b2b2b;
    --grey-word: #8a8a8a;
    --swoosh-grey: #3a3a3a;
    --icon-blue: #3d3f96;
  }
  * { margin: 0; padding: 0; box-sizing: border-box; }
  html, body { width: 1200px; height: 900px; overflow: hidden; }
  body { background: var(--page-bg); position: relative; font-family: "Exo 2", sans-serif; }

  .business-card {
    position: absolute; left: 100px; top: 165px;
    width: 1000px; height: 570px;
    background: var(--card-bg);
    border-radius: 56px;
    overflow: hidden;
    box-shadow: 0 10px 30px rgba(0,0,0,0.12);
  }
  .card-swoosh { position: absolute; inset: 0; }

  .brand-block {
    position: absolute; left: 70px; top: 100px; width: 320px;
    text-align: center;
  }
  .brand-circle {
    width: 170px; height: 170px; border-radius: 50%;
    background: var(--brand-blue);
    margin: 0 auto 22px;
  }
  .brand-name {
    font-family: "Open Sans", sans-serif; font-weight: 700;
    font-size: 38px; color: var(--grey-word); letter-spacing: 1px;
    line-height: 1.1;
  }

  .contact-block { position: absolute; left: 560px; top: 42px; color: var(--ink); }
  .person-name {
    font-family: "Exo 2", sans-serif; font-weight: 500; font-size: 27px;
    color: var(--name-blue); letter-spacing: 1.5px; text-transform: uppercase;
  }
  .person-title { font-size: 21px; margin-top: 2px; }
  .postal-address { font-style: normal; font-size: 19px; line-height: 26px; margin-top: 34px; margin-left: 32px; }
  .contact-list { list-style: none; margin-top: 28px; margin-left: 50px; font-size: 18px; }
  .contact-list li { display: flex; align-items: center; gap: 12px; height: 26px; }
  .contact-icon { width: 16px; height: 16px; fill: var(--icon-blue); flex: none; }
</style>
</head>
<body>
  <div class="business-card">
    <svg class="card-swoosh" viewBox="0 0 1000 570" aria-hidden="true">
      <defs>
        <linearGradient id="bandGradient" x1="0" y1="0" x2="1" y2="0">
          <stop offset="0" stop-color="var(--band-deep)"/>
          <stop offset="0.55" stop-color="#2f6fd0"/>
          <stop offset="1" stop-color="var(--band-light)"/>
        </linearGradient>
        <path id="bandTextPath" d="M300,548 C520,500 760,430 980,395"/>
      </defs>
      <path d="M0,570 L0,560 C260,545 620,440 1000,360 L1000,570 Z" fill="url(#bandGradient)"/>
      <path d="M0,548 C260,532 620,425 1000,344" fill="none" stroke="var(--swoosh-grey)" stroke-width="7"/>
      <path d="M0,556 C260,540 620,434 1000,353" fill="none" stroke="#ffffff" stroke-width="4"/>
      <text font-family="Open Sans, sans-serif" font-size="22" fill="#ffffff" letter-spacing="4">
        <textPath href="#bandTextPath">www.trwdevelopments.co.uk</textPath>
      </text>
    </svg>

    <div class="brand-block">
      <div class="brand-circle"></div>
      <div class="brand-name">TRW DEVELOPMENTS</div>
    </div>

    <div class="contact-block">
      <h1 class="person-name">Dermot Aldwick</h1>
      <p class="person-title">Managing Director</p>
      <address class="postal-address">58 Fennick Lane,<br>Ipswich IP7 2DX</address>
      <ul class="contact-list">
        <li><svg class="contact-icon" viewBox="0 0 16 16"><path d="M3 1l3 3-2 2c1 2 3 4 5 5l2-2 3 3-2 3C6 15 1 10 1 3z"/></svg>01473 555 014</li>
        <li><svg class="contact-icon" viewBox="0 0 16 16"><path d="M4 0h8a1 1 0 0 1 1 1v14a1 1 0 0 1-1 1H4a1 1 0 0 1-1-1V1a1 1 0 0 1 1-1zm1 2v10h6V2zm3 11a1 1 0 1 0 0 2 1 1 0 0 0 0-2z"/></svg>07700 900 382</li>
        <li><svg class="contact-icon" viewBox="0 0 16 16"><path d="M3 0h8v5H3zM1 6h14v10H1zm3 2v2h2V8zm4 0v2h2V8zm-4 4v2h2v-2zm4 0v2h2v-2z"/></svg>01473 555 015</li>
        <li><svg class="contact-icon" viewBox="0 0 16 16"><path d="M0 3h16v10H0zm1 1l7 5 7-5z" fill-rule="evenodd"/></svg>hello@trwdevelopments.co.uk</li>
        <li><svg class="contact-icon" viewBox="0 0 16 16"><path d="M8 0a8 8 0 1 0 0 16A8 8 0 0 0 8 0zm-1 1.2C5.5 3 5 5 5 7h2zm2 0V7h2c0-2-.5-4-2-5.8zM2 9a6 6 0 0 0 4 5C5 12.5 5 11 5 9zm9 0c0 2 0 3.5-1 5a6 6 0 0 0 4-5zM7 9H6c0 2 .3 3.5 1 5zm2 0v5c.7-1.5 1-3 1-5zM1.1 7H4c0-2 .5-3.7 1.4-5.2A6 6 0 0 0 1.1 7zm9.5-5.2C11.5 3.3 12 5 12 7h2.9a6 6 0 0 0-4.3-5.2z"/></svg>www.trwdevelopments.co.uk</li>
      </ul>
    </div>
  </div>
</body>
</html>
```